依頼詳細
《チラシのイメージ》
複数の写真やイラストの使用は避けてください。子育て世代向けへの広告とは一線画した差別化されたデザインを希望しています。また、子どもにフォーカスするのではなく、子育てママをフォーカスしていると一目でわかるビジュアルに仕上げてください。

※前回は塗り絵を前面に押しましたが、今回はその必要はありません。
(前回のチラシは添付データーをご参照ください)
理由は、前回は塗り絵に興味がある人への告知になってましたが、今回は子育てする親がセミナーに参加したくなるものにしてください。
《ターゲット》
お子さんの年齢は6歳以下の未就学児がいる中間層の子育て家族。

《デザインへの希望》
フォントのデザイン・文字サイズにメリハリをつけてください。
広告を見た瞬間に詳しく読みたくなるキャッチをメインにして「いつ開催?」「どこで開催?」は分かり易く見易く、その後、詳しく読みたくなる部分や、参加希望する人が必ず確認する部分については、小さな文字にしていただくことで、デザイン構成ください。

参加費無料や定員など、営業に映るような部分も、当会は堺貢献事業として活動している団体のため、営業的に映る部分については大きく目立つ表記は避けてください。さりげなく表記いただき、見れば分かる記述で結構です。

いろんな色を使用することで、ゴチャゴチャして大切な部分が見えなくなってしまうのは避けてください。

《セミナー構成》
前半:親への子育てセミナー
後半:子ども塗り絵診断

【キャッチ】
▮子どもと「ちょうどいい」距離感
または
▮子どもの世界をつくる
ママのひとり時間をつくる

【サブキャッチ】
▮子どもが言葉を話すようになったら...それは自分の世界を広げたいサイン

【リード文】
▮子育ての順番は「手を掛ける」「目を掛ける」「気を掛ける」どのタイミングでステップアップするかは、それぞれの子どもによって違う。子育てについて「周りは?」ついそう思ってしまいがち。周りを気にするのは誰かと比較してること。もっと色んな視点から子どもを見つめてみると見えてくるもの。早くから子どもの世界づくりをはじめ、親も自分時間を持つことで親子のちょうどいい距離感が生まれる。

【セミナー内容】
Lesson1ママパパ学び
・子どもの世界
・子どもの世界を広げるタイミング
・ヤル気のONスイッチ
・ちょうどいい子どもとの距離感
・子どもが成長してしまう3つのアプロ―チ
・子育て計画「コト・モノ・オカネ」

Lesson2子ども学び
・個性を見つける10の視点
・塗り絵診断
・子どもは天才の卵!
・生まれもった性格

【詳細】
テーマ:はじめての習いごと
開催日:8月24日(土)
時間:14時~16時
参加費:無料
定員:8家族(夫婦・親子でご参加ください)
開催場所:北嶺市民活動センター「ひだまる」
(兵庫県加古川市緑野町桜台字松ノ木45-3)
対象者:子ども年齢/1歳2か月~6歳
(参加にはお申込みが必要です)
主催:そらいるか(一般社団法人家庭育成推進協会)
後援:加古川市 緑沢市教育委員会
講師:そらいるか認定講師
受付:そらいるか事務局
〒541-0093大阪市中央区東浜町3-2-5-208
TEL0120-870-041
06-6912-4537    ※電話受付は平日9時~17時のみ
(メールは不要)

ホームページからのお申込みは▼
QRコード

記載項目
主催:そらいるか(一般社団法人家庭育成推進協会)
〒541-0093 大阪府大阪市中央区東浜町3-2-5-208
TEL:06-6912-4537 FAX:06-6912-4538
サイズ
A4
ページ数
片面
希望イメージ
シンプル 複雑
単色 カラフル
暗い 明るい
日常 高級
遊び心 厳粛
未来的 伝統的
女性的 男性的
希望する色
黄・オレンジ系
納品ファイル
• イラストレーター形式 (.ai)
補足説明
今回のセミナーは、過去に何度も開催しており、少しづつブラッシュアップしていってます。ワークポッドを利用するのは今回で2回目です。前回は21,600円でコンペに出しましたが、今回は要望内容が多いため54,000円でコンペに応募します。
現在、加古川市と緑沢市教育委員会に後援申請をしています。後援の許可の有無により、後援名の部分の修正をお願いする可能性があります。またご提案いただいたチラシ内容は、法人の理事長の許可を必要としますので何度か修正をお願いすると思います。ご質問等がありましたら、ご連絡ください。

スッキリとまとまっており、一番目に飛び込んでくる構成になっているところが良かったです。
また、修正する場合に作業がしやすいデザインになっていると思えたところが良かったです。

沢山提案していただきありがとうございました。
また、こちらの都合で決めるのに時間がかかり申し訳ありませんでした。

```html
<!DOCTYPE html>
<html lang="ja">
<head>
<meta charset="utf-8">
<title>子育てセミナー はじめての習い事</title>
<link href="https://fonts.googleapis.com/css2?family=Noto+Sans+JP:wght@400;500;700;900&family=Noto+Serif+JP:wght@500;700&display=swap" rel="stylesheet">
<style>
:root{
  --orange:#e9822c;
  --orange-deep:#d96a17;
  --orange-soft:#fbe3cb;
  --cream:#fdf8f1;
  --ink:#4b3a2f;
  --ink-soft:#7a6658;
  --line:#e4cdb6;
  --white:#ffffff;
}
*{box-sizing:border-box;margin:0;padding:0}
html,body{width:849px;height:1200px;overflow:hidden}
body{background:var(--cream);font-family:"Noto Sans JP",sans-serif;color:var(--ink)}
.flyer{position:relative;width:849px;height:1200px;overflow:hidden;background:var(--cream)}

.hero-photo{position:absolute;left:0;top:0;width:450px;height:550px;
  background:linear-gradient(90deg,#b98768 0%,#cfa384 45%,#e9d3bf 80%,rgba(253,248,241,0) 100%),
             linear-gradient(180deg,#a86d47 0%,#cf9f7b 55%,#f2e4d4 100%);}
.hero-photo::after{content:"";position:absolute;inset:0;
  background:linear-gradient(180deg,rgba(253,248,241,0) 75%,var(--cream) 100%),
             linear-gradient(90deg,rgba(253,248,241,0) 80%,var(--cream) 100%)}

.catch-top{position:absolute;left:230px;top:14px;width:390px;text-align:center;font-family:"Noto Serif JP",serif;font-size:22px;font-weight:700;color:var(--ink);letter-spacing:.12em;background:var(--white);padding:6px 0;border-top:2px solid var(--orange);border-bottom:2px solid var(--orange)}
.catch-sub{position:absolute;left:165px;top:115px;width:330px;text-align:center;font-family:"Noto Serif JP",serif;font-size:20px;font-weight:700;color:var(--ink);letter-spacing:.1em;background:rgba(255,255,255,.9);padding:4px 0}

.sub-copy{position:absolute;left:42px;top:360px;color:var(--white);font-family:"Noto Serif JP",serif;font-weight:700;font-size:20px;line-height:1.9;letter-spacing:.08em;text-shadow:0 1px 3px rgba(0,0,0,.3)}

.badge{position:absolute;left:738px;top:150px;width:104px;height:104px;border-radius:50%;background:var(--orange);color:var(--white);display:flex;flex-direction:column;align-items:center;justify-content:center;font-weight:900;line-height:1.2;text-align:center}
.badge .num{font-size:22px}
.badge .txt{font-size:15px}

.title{position:absolute;left:428px;top:188px;font-size:40px;font-weight:900;letter-spacing:.04em;color:var(--ink);white-space:nowrap}
.theme{position:absolute;left:428px;top:246px;width:300px;text-align:center}
.theme .label{display:block;font-size:14px;font-weight:700;color:var(--ink)}
.theme .name{display:block;font-size:28px;font-weight:900;color:var(--orange-deep);letter-spacing:.05em}
.date{position:absolute;left:425px;top:440px;display:flex;align-items:flex-end;gap:12px;color:var(--orange-deep)}
.date .day{font-size:88px;font-weight:900;line-height:1;letter-spacing:-.02em}
.date .time{font-size:24px;font-weight:700;line-height:1.35;padding-bottom:6px}
.date .time small{font-size:14px;color:var(--ink)}

.lead{position:absolute;left:40px;top:572px;width:350px;font-size:14px;line-height:2;color:var(--ink)}
.lead p{margin-bottom:8px}

.details{position:absolute;left:425px;top:560px;width:400px;border-collapse:collapse;font-size:13px}
.details th{width:90px;text-align:left;vertical-align:top;font-weight:700;padding:7px 0 9px;color:var(--ink);border-bottom:1px solid var(--line)}
.details td{padding:7px 0 9px;border-bottom:1px solid var(--line);line-height:1.45}
.details .venue{font-size:15px;font-weight:700}
.details .note{font-size:11px;color:var(--ink-soft)}
.details .free{font-size:17px;font-weight:700}

.lessons{position:absolute;left:14px;top:952px;width:821px;display:flex;gap:14px}
.lesson{background:var(--white);border:2px solid var(--orange);flex:1}
.lesson-1{flex:1.25}
.lesson h3{background:var(--orange);color:var(--white);font-size:15px;font-weight:700;padding:4px 10px;letter-spacing:.04em}
.lesson h3 span{margin-right:6px}
.lesson ul{list-style:none;display:grid;grid-template-columns:1fr 1fr;gap:3px 8px;padding:8px 10px 10px}
.lesson li{font-size:11.5px;line-height:1.5}
.lesson li::before{content:"・";color:var(--orange)}

.footer{position:absolute;left:0;top:1075px;width:849px;height:125px;background:var(--white);border-top:2px solid var(--orange-soft)}
.mark{position:absolute;left:22px;top:25px;width:66px;height:66px;border-radius:50%;background:var(--orange)}
.office{position:absolute;left:98px;top:30px;font-size:22px;font-weight:900;color:var(--ink)}
.office-org{position:absolute;left:98px;top:66px;font-size:10px;color:var(--ink-soft)}
.phone{position:absolute;left:300px;top:22px;display:flex;align-items:center;gap:8px;color:var(--orange-deep)}
.phone .num{font-size:38px;font-weight:900;letter-spacing:.01em}
.phone-sub{position:absolute;left:340px;top:76px;font-size:12px;color:var(--ink)}
.hours{position:absolute;left:668px;top:30px;font-size:12px;line-height:1.4;color:var(--ink)}
.apply{position:absolute;left:600px;top:82px;width:170px;font-size:10px;color:var(--ink);text-align:right}
.qr{position:absolute;left:778px;top:26px;width:60px;height:60px;background:var(--white);border:4px solid var(--ink)}
</style>
</head>
<body>
<div class="flyer">
  <div class="hero-photo" role="img" aria-label="窓辺で微笑む子育て中の母親の写真"></div>

  <div class="catch-top">子供の世界を作る</div>
  <div class="catch-sub">ママの一人時間を作る</div>

  <p class="sub-copy">子供が言葉を<br>話すようになったら…<br>それは自分の世界を<br>広げたいサイン</p>

  <div class="badge"><span class="num">8家族</span><span class="txt">限定の<br>学び場</span></div>

  <h1 class="title">子育てセミナー</h1>
  <div class="theme"><span class="label">テーマ</span><span class="name">はじめての習い事</span></div>

  <div class="date">
    <span class="day">8.24</span>
    <span class="time">14:00~16:00<br>(月) <small>受付 13:45~</small></span>
  </div>

  <div class="lead">
    <p>子育ての順番は「手を掛ける」「目を掛ける」「気を掛ける」どのタイミングでステップアップするかは、それぞれの子どもによって違う。</p>
    <p>子育てについて「周りは？」ついそう思ってしまいがち。周りを気にするのは誰かと比較してること。もっと色んな視点から子どもを見つめてみると見えてくるもの。</p>
    <p>早くから子どもの世界づくりをはじめ、親も自分時間を持つことで親子のちょうどいい距離感が生まれる。</p>
  </div>

  <table class="details">
    <tr><th>開催場所</th><td><span class="venue">北嶺市民活動センター「ひだまる」</span><br><span class="note">(兵庫県加古川市緑野町桜台字松ノ木45-3)</span></td></tr>
    <tr><th>参加費</th><td class="free">無料</td></tr>
    <tr><th>対象者</th><td>子供年齢 / 1歳2ヵ月～6歳<br><span class="note">参加にはお申し込みが必要です。<br>夫婦・親子でご参加ください。</span></td></tr>
    <tr><th>講　師</th><td>そらいるか講師</td></tr>
    <tr><th>後　援</th><td>加古川市、緑沢市教育委員会</td></tr>
    <tr><th>主　催</th><td>そらいるか<br><span class="note">(一般社団法人家庭育成推進協会)<br>〒541-0093 大阪府大阪市中央区東浜町3-2-5-208</span></td></tr>
  </table>

  <div class="lessons">
    <section class="lesson lesson-1">
      <h3><span>Lesson1</span>ママパパ学び</h3>
      <ul>
        <li>子供の世界</li>
        <li>丁度よい子供との距離感</li>
        <li>子供の世界を広げるタイミング</li>
        <li>子供が成長する３つのアプローチ</li>
        <li>ヤル気のオンスイッチ</li>
        <li>子育て計画「コト・モノ・オカネ」</li>
      </ul>
    </section>
    <section class="lesson lesson-2">
      <h3><span>Lesson2</span>子供学び</h3>
      <ul>
        <li>個性を見つける10の視点</li>
        <li>子供は天才の卵！</li>
        <li>塗り絵診断</li>
        <li>生まれもった性格</li>
      </ul>
    </section>
  </div>

  <footer class="footer">
    <div class="mark"></div>
    <div class="office">そらいるか事務所</div>
    <div class="office-org">(一般社団法人家庭育成推進協会)</div>
    <div class="phone">
      <svg width="32" height="32" viewBox="0 0 24 24" aria-hidden="true"><path fill="#d96a17" d="M6.6 10.8a15.1 15.1 0 0 0 6.6 6.6l2.2-2.2a1 1 0 0 1 1-.25 11.4 11.4 0 0 0 3.6.57 1 1 0 0 1 1 1V20a1 1 0 0 1-1 1A17 17 0 0 1 3 4a1 1 0 0 1 1-1h3.5a1 1 0 0 1 1 1c0 1.250.2 2.45.57 3.57a1 1 0 0 1-.25 1z"/></svg>
      <span class="num">0120-354-926</span>
    </div>
    <div class="phone-sub">(TEL) 06-6912-4537</div>
    <div class="hours">受付 平日<br>9:00-17:00</div>
    <div class="apply">ホームページからお申し込み▶</div>
    <div class="qr" role="img" aria-label="申し込みページのQRコード"></div>
  </footer>
</div>
</body>
</html>
```